Mobile (Android/iPhone) game studio needs stationary design and a business card

We are Plunk Ferret Software and we need a fun and creative stationary design. Our company builds Android and iPhone games and children's software. The stationary designs should reflect an entertainment, fun and creativity. The pieces of stationary we need are:
1. A4 and Letter Word template (company letterhead)
2. A4 and Letter PPT template
3. Business card
4. Envelopes of various standard sizes
Each of the designs should somehow utilize our company logo.
The business card should have the following:
1. Incorporates our company logo (see attached)
2. Has a front and back with the same design (front is English, back is Traditional Chinese)
3. Delivered in an editable template so we can easily add new business cards using the same template when we hire more employees
4. Field for full name
5. Field for employee's title
6. Field for employee's email address
7. Field for company phone number - +886-2-51384470
8. Field for mobile phone number
9. Field for company fax number - +886-2-51384492
10. Company website address: www.plunkferret.example
11. Company address (on English side): 7F-2, NO. 63, Lane 91, Guoyuan Road, Dali District, Taipei Taiwan
12. Company address (on Traditional Chinese side): See Word document attachment for address in Chinese characters
Industry/Entity Type
Games
Look and feel
Each slider illustrates characteristics of the customer's brand and the style your logo design should communicate.

```html
<!DOCTYPE html>
<html lang="en">
<head>
<meta charset="utf-8">
<title>Plunk Ferret Software – Envelopes</title>
<link href="https://fonts.googleapis.com/css2?family=Exo+2:wght@400;600;700&display=swap" rel="stylesheet">
<style>
  :root {
    --board-frame: #ffffff;
    --board: #e4e4e4;
    --paper: #ffffff;
    --sky: #5cc6f2;
    --brand-blue: #1b8ed6;
    --ink: #555a5e;
    --label: #5bbfe9;
    --window: #fff7bd;
    --ghost: #ececec;
  }
  * { margin: 0; padding: 0; box-sizing: border-box; }
  html, body { width: 1200px; height: 854px; overflow: hidden; background: var(--board-frame); }
  .board {
    position: absolute; left: 8px; top: 8px; width: 1184px; height: 838px;
    background: var(--board);
  }
  .envelope {
    position: absolute; width: 621px; height: 383px;
    filter: drop-shadow(0 3px 4px rgba(0,0,0,.22));
    font-family: "Exo 2", sans-serif;
  }
  .envelope--plain { left: 103px; top: 122px; }
  .envelope--window { left: 478px; top: 377px; }
  .envelope__body { position: absolute; inset: 0; width: 621px; height: 383px; }
  .envelope__mascot-area {
    position: absolute; left: 52px; top: 214px; width: 250px; height: 169px;
    background: radial-gradient(ellipse at 50% 70%, #e9e9e9 0%, #f1f1f1 45%, rgba(255,255,255,0) 72%);
  }
  .envelope__url {
    position: absolute; left: 0; top: 26px; width: 621px; text-align: center;
    color: var(--sky); font-weight: 700; font-size: 19px; letter-spacing: .3px;
    transform: rotate(180deg);
  }
  .brand {
    position: absolute; left: 17px; top: 112px; display: flex; align-items: center; gap: 8px;
  }
  .brand__dot { width: 24px; height: 24px; border-radius: 50%; background: var(--brand-blue); }
  .brand__name { color: var(--brand-blue); font-weight: 600; font-size: 17px; }
  .contact {
    position: absolute; left: 20px; top: 165px;
    display: grid; grid-template-columns: 54px auto; column-gap: 6px;
    font-size: 8.6px; line-height: 10.6px;
  }
  .contact dt { color: var(--label); text-align: right; }
  .contact dd { color: var(--ink); }
  .envelope__window {
    position: absolute; left: 283px; top: 200px; width: 281px; height: 126px;
    background: var(--window); border-radius: 8px;
  }
</style>
</head>
<body>
<main class="board">

  <section class="envelope envelope--plain">
    <svg class="envelope__body" viewBox="0 0 621 383" aria-hidden="true">
      <path d="M0,73 L34,10 Q40,0 52,0 L569,0 Q581,0 587,10 L621,73 L621,383 L0,383 Z" fill="var(--paper)"/>
    </svg>
    <div class="envelope__mascot-area" role="img" aria-label="Faint mascot decoration in light grey"></div>
    <p class="envelope__url">www.plunkferret.example</p>
    <div class="brand"><span class="brand__dot"></span><span class="brand__name">Plunk Ferret Software</span></div>
    <dl class="contact">
      <dt>Address</dt><dd>7F-2, NO. 63, Lane 91</dd>
      <dt></dt><dd>Guoyuan Road, Dali District</dd>
      <dt></dt><dd>Taipei Taiwan</dd>
      <dt>Phone</dt><dd>+886-2-51384470</dd>
      <dt>Fax</dt><dd>+886-2-51384492</dd>
    </dl>
  </section>

  <section class="envelope envelope--window">
    <svg class="envelope__body" viewBox="0 0 621 383" aria-hidden="true">
      <path d="M0,73 L34,10 Q40,0 52,0 L569,0 Q581,0 587,10 L621,73 L621,383 L0,383 Z" fill="var(--paper)"/>
    </svg>
    <div class="envelope__mascot-area" role="img" aria-label="Faint mascot decoration in light grey"></div>
    <p class="envelope__url">www.plunkferret.example</p>
    <div class="brand"><span class="brand__dot"></span><span class="brand__name">Plunk Ferret Software</span></div>
    <dl class="contact">
      <dt>Address</dt><dd>7F-2, NO. 63, Lane 91</dd>
      <dt></dt><dd>Guoyuan Road, Dali District</dd>
      <dt></dt><dd>Taipei Taiwan</dd>
      <dt>Phone</dt><dd>+886-2-51384470</dd>
      <dt>Fax</dt><dd>+886-2-51384492</dd>
    </dl>
    <div class="envelope__window"></div>
  </section>

</main>
</body>
</html>
```